Business card for Delacroft Anesthesia LLC

This is for a business care for Delacroft Anesthesia LLC. Dr. Helen Delacroft, CRNA, DNAP is the sole provider in the LLC. Business address is 4716 N Brackley Avenue,
Ashmoor, PA 17642
CRNA stands for certified registered nurse anesthetist
"Keeping you safe and comfortable"
I plan to give this business card to the patients that I provide anesthesia to.
Creative design that ties into Anesthesia. Calm soothing colors.

Target Market(s)

Business card for my patients.

Industry/Entity Type

Medicine

Contact Information for Business Card

Creative, professional, eye catching

Logo Text

Delacroft Anesthesia

Font styles to use
Serif
Script

Colors

Designer to choose colors to be used in the design.

Requirements
Must have
• Delacroft Anesthesia
• Dr. Helen Delacroft, CRNA, DNAP
• delacroft.anesthesia@ quillmail.net
Nice to have
• "Keeping you safe and comfortable"
Should not have
• phone number

```html
<!DOCTYPE html>
<html lang="en">
<head>
<meta charset="utf-8">
<title>Delacroft Anesthesia LLC – Business Card</title>
<link rel="stylesheet" href="https://fonts.googleapis.com/css2?family=Cinzel:wght@600&family=Marcellus&family=Lato:wght@400&display=swap">
<style>
  :root {
    --backdrop: #9a9a9a;
    --paper: #ffffff;
    --navy: #27548a;
    --leaf: #5b9a1c;
    --ink: #333333;
    --rule: #d4d4d4;
  }
  * { margin: 0; padding: 0; box-sizing: border-box; }
  html, body {
    width: 1200px; height: 900px; overflow: hidden;
    background: var(--backdrop);
  }
  .stage { position: relative; width: 1200px; height: 900px; }

  .card-front {
    position: absolute; left: 121px; top: 275px;
    width: 476px; height: 294px;
    background: var(--paper);
    border-radius: 0 58px 0 58px;
    font-family: "Lato", sans-serif;
  }
  .brand {
    position: absolute; right: 26px; top: 47px;
    display: flex; align-items: center; gap: 12px;
  }
  .brand-mark {
    width: 70px; height: 70px; border-radius: 50%;
    border: 3px solid var(--navy);
    flex: none;
  }
  .brand-name {
    font-family: "Marcellus", serif;
    color: var(--navy);
    line-height: 1;
    text-transform: uppercase;
    white-space: nowrap;
  }
  .brand-name .primary { display: block; font-size: 32px; letter-spacing: 0.5px; }
  .brand-name .secondary { display: block; font-size: 18.5px; letter-spacing: 1.6px; margin-top: 4px; }

  .holder {
    position: absolute; left: 24px; top: 148px;
    font-family: "Cinzel", serif; font-weight: 600;
    color: var(--navy); font-size: 19px; letter-spacing: 0.3px;
    white-space: nowrap;
  }
  .holder .credentials { font-size: 14.5px; }
  .rule {
    position: absolute; left: 24px; width: 426px; height: 1.5px;
    background: var(--rule);
  }
  .rule-top { top: 176px; }
  .rule-bottom { top: 235px; }
  .contact {
    position: absolute; left: 24px;
    display: flex; align-items: center; gap: 6px;
    font-size: 13.5px; color: var(--ink);
    white-space: nowrap;
  }
  .contact svg { flex: none; }
  .contact-email { top: 183px; }
  .contact-address { top: 210px; }
  .tagline {
    position: absolute; left: 26px; top: 247px;
    font-size: 14px; color: var(--navy); text-transform: uppercase;
  }

  .card-back {
    position: absolute; left: 607px; top: 274px;
    width: 476px; height: 293px;
    background: var(--navy);
    border-radius: 58px 0 58px 0;
    display: flex; align-items: center; justify-content: center; gap: 12px;
  }
  .card-back .brand-mark { border-color: var(--paper); }
  .card-back .brand-name { color: var(--paper); }
</style>
</head>
<body>
<div class="stage">
  <section class="card-front">
    <div class="brand">
      <div class="brand-mark"></div>
      <div class="brand-name">
        <span class="primary">Delacroft</span>
        <span class="secondary">Anesthesia LLC</span>
      </div>
    </div>
    <p class="holder">DR. HELEN DELACROFT<span class="credentials">, CRNA, DNAP</span></p>
    <div class="rule rule-top"></div>
    <p class="contact contact-email">
      <svg width="10" height="8" viewBox="0 0 10 8"><rect width="10" height="8" fill="var(--leaf)"/><path d="M0.6 0.8 5 4.3 9.4 0.8" stroke="#fff" stroke-width="1.1" fill="none"/></svg>
      delacroft.anesthesia@ quillmail.net
    </p>
    <p class="contact contact-address">
      <svg width="9" height="13" viewBox="0 0 9 13"><path fill="var(--leaf)" d="M4.5 0A4.5 4.5 0 0 0 0 4.5C0 8 4.5 13 4.5 13S9 8 9 4.5A4.5 4.5 0 0 0 4.5 0zm0 6.3a1.8 1.8 0 1 1 0-3.6 1.8 1.8 0 0 1 0 3.6z"/></svg>
      4716 N Brackley Avenue Ashmoor, PA 17642
    </p>
    <div class="rule rule-bottom"></div>
    <p class="tagline">Keeping you safe and comfortable</p>
  </section>

  <section class="card-back">
    <div class="brand-mark"></div>
    <div class="brand-name">
      <span class="primary">Delacroft</span>
      <span class="secondary">Anesthesia LLC</span>
    </div>
  </section>
</div>
</body>
</html>
```